Modern Spot UV Business Card design

We are a relatively new real estate agency. We need a business card that reflects the professionalism and prestige of our company but is also modern and fresh, based around our logo.
We would love to utilise spot UV.
Happy to let the designers use their imagination and see what they come up with (we're not very creative, so have no ideas for you, sorry) :-)
We'd like one for each staff member, but I've just provided one staff members photo here to avoid confusion.

Target Market(s)

Families

Industry/Entity Type

Real Estate Agent

Contact Information for Business Card

Colin Varga - Director & Principal
Mobile: 0491 527 806
Email: colin.varga@vbrokers.example.com.au
Phone: (08) 7364 9150
Fax: (08) 7364 9182
www.vargabrokersrealestate.example.com.au

Font styles to use
Other font styles liked:
• Kabel Dm BT

Requirements
Must have
• Contact details, logo, photo, spot UV
Nice to have
• Modern interesting features that will make people comment. Nothing too feminine nor too masculine.
Should not have
• No houses! Nothing typical of a real estate agent.

```html
<!DOCTYPE html>
<html lang="en">
<head>
<meta charset="utf-8">
<title>Varga Brokers – Business Card</title>
<link rel="stylesheet" href="https://fonts.googleapis.com/css2?family=Lato:wght@400;700&display=swap">
<style>
  :root {
    --stage: #e9e6e2;
    --card-dark: #1f1e1f;
    --card-light: #ffffff;
    --ink: #2b2b2b;
    --ink-soft: #555555;
    --accent: #1a8fd6;
    --uv-gloss: #3b3a3b;
    --sun-soft: #fdf3cc;
    --roof-soft: #dcdcdc;
  }
  * { box-sizing: border-box; margin: 0; padding: 0; }
  html, body { width: 1200px; height: 849px; overflow: hidden; }
  body {
    background: var(--stage);
    font-family: "Lato", sans-serif;
    position: relative;
  }
  .card {
    position: absolute;
    left: 272px;
    width: 632px;
    height: 354px;
    border-radius: 20px;
    overflow: hidden;
    box-shadow: 0 4px 12px rgba(0,0,0,0.25);
  }
  .card--back { top: 40px; background: var(--card-dark); }
  .card--front { top: 440px; background: var(--card-light); }

  .brand-name {
    position: absolute;
    font-family: "Lato", sans-serif;
    font-weight: 700;
    white-space: nowrap;
  }
  .card--back .brand-name {
    left: 0; right: 0; top: 150px;
    text-align: center;
    font-size: 46px;
    color: var(--uv-gloss);
  }
  .card--back .website {
    position: absolute;
    left: 0; right: 0; top: 296px;
    text-align: center;
    font-size: 15px;
    color: #ffffff;
  }
  .website .domain { color: var(--accent); }

  .card--front .brand-name {
    right: 42px; top: 64px;
    font-size: 40px;
    color: var(--ink);
  }
  .person { position: absolute; left: 42px; top: 50px; }
  .person__name { font-size: 24px; font-weight: 700; color: var(--accent); line-height: 1.1; }
  .person__role { font-size: 14px; color: var(--ink-soft); margin-top: 3px; }

  .contacts { position: absolute; left: 42px; top: 226px; list-style: none; }
  .contacts li {
    display: flex; align-items: center;
    height: 20px;
    font-size: 14px; color: var(--ink-soft);
  }
  .contacts svg { width: 14px; height: 14px; margin-right: 8px; fill: var(--accent); flex: none; }

  .corner-art {
    position: absolute;
    left: 408px; top: 160px;
    width: 256px; height: 256px;
    border-radius: 50%;
    background: linear-gradient(160deg, var(--sun-soft) 55%, var(--roof-soft) 100%);
  }
</style>
</head>
<body>
  <section class="card card--back">
    <div class="brand-name">Varga Brokers</div>
    <div class="website">www.<span class="domain">vargabrokersrealestate</span>.example.com.au</div>
  </section>

  <section class="card card--front">
    <div class="person">
      <div class="person__name">Colin Varga</div>
      <div class="person__role">Director &amp; Principal</div>
    </div>
    <div class="brand-name">Varga Brokers</div>

    <ul class="contacts">
      <li><svg viewBox="0 0 16 16"><path d="M3 1l3 3-1.5 2a9 9 0 0 0 5.5 5.5L12 10l3 3-2 2C7 15 1 9 1 3z"/></svg>(08) 7364 9150</li>
      <li><svg viewBox="0 0 16 16"><path d="M4 1h8v14H4zM5.5 2.5v9h5v-9zM7 12.5h2v1H7z" fill-rule="evenodd"/></svg>0491 527 806</li>
      <li><svg viewBox="0 0 16 16"><path d="M4 1h8v4H4zM1 6h14v6h-3v3H4v-3H1zM5 10v4h6v-4z" fill-rule="evenodd"/></svg>(08) 7364 9182</li>
      <li><svg viewBox="0 0 16 16"><path d="M1 4h14v9H1zM1 4l7 5 7-5"/></svg>colin.varga@vbrokers.example.com.au</li>
      <li><svg viewBox="0 0 16 16"><path d="M8 1a7 7 0 1 0 0 14A7 7 0 0 0 8 1zm0 1.5c.8 0 1.8 1.8 2 4.5H6c.2-2.7 1.2-4.5 2-4.5zM2.6 7h2c.1-1.8.5-3.3 1.1-4.2A5.5 5.5 0 0 0 2.6 7zm7.7-4.2c.6.9 1 2.4 1.1 4.2h2a5.5 5.5 0 0 0-3.1-4.2zM2.6 9a5.5 5.5 0 0 0 3.1 4.2C5.1 12.3 4.7 10.8 4.6 9zm3.4 0c.2 2.7 1.2 4.5 2 4.5s1.8-1.8 2-4.5zm5.4 0c-.1 1.8-.5 3.3-1.1 4.2A5.5 5.5 0 0 0 13.4 9z" fill-rule="evenodd"/></svg>www.vargabrokersrealestate.example.com.au</li>
    </ul>

    <div class="corner-art" role="img" aria-label="Soft yellow sun with a pale grey roofline decoration"></div>
  </section>
</body>
</html>
```